Commercial Construction Company

We need a business card design based on our current logo. We are a commercial general contractor based in Southern California that specializes in bank remodels. We would like to see designs that incorporate dark blue. The final design should portray an image of professionalism and quality.

If possible, I would like to add metallic foil to the design. Thank you

```html
<!DOCTYPE html>
<html lang="en">
<head>
<meta charset="utf-8">
<title>Halden Commercial Builders – Business Card</title>
<link rel="stylesheet" href="https://fonts.googleapis.com/css2?family=Montserrat:wght@300;400;600&display=swap">
<style>
  :root {
    --navy: #0f1d38;
    --navy-line: #1c2d4f;
    --teal: #4fb3a6;
    --teal-soft: #7fcbc0;
    --page: #ffffff;
  }
  * { margin: 0; padding: 0; box-sizing: border-box; }
  html, body {
    width: 1200px;
    height: 1199px;
    overflow: hidden;
    background: var(--page);
    font-family: "Montserrat", sans-serif;
  }
  .sheet {
    position: relative;
    width: 1200px;
    height: 1199px;
  }
  .card {
    position: absolute;
    top: 443px;
    width: 520px;
    height: 312px;
    background: var(--navy);
    overflow: hidden;
  }
  .card--front { left: 50px; }
  .card--back { left: 630px; }

  .block { position: absolute; background: var(--teal); }

  /* front */
  .front-brand {
    position: absolute;
    left: 0; right: 0;
    top: 128px;
    display: flex;
    align-items: center;
    justify-content: center;
    gap: 12px;
    color: var(--teal);
  }
  .brand-dot {
    width: 22px; height: 22px;
    border-radius: 50%;
    background: var(--teal);
  }
  .brand-name {
    font-weight: 600;
    font-size: 34px;
    letter-spacing: 2px;
  }

  /* back */
  .drawing-area {
    position: absolute;
    left: 75px; top: 0;
    width: 330px; height: 312px;
    background: linear-gradient(180deg, rgba(28,45,79,0) 0%, rgba(28,45,79,0.55) 45%, rgba(28,45,79,0.25) 100%);
  }
  .back-brand {
    position: absolute;
    right: 36px; top: 40px;
    display: flex;
    align-items: center;
    gap: 5px;
    color: var(--teal);
  }
  .back-brand .brand-dot { width: 10px; height: 10px; }
  .back-brand .brand-name { font-size: 13px; letter-spacing: 1px; }

  .identity {
    position: absolute;
    left: 0; right: 0;
    top: 76px;
    text-align: center;
    color: var(--teal);
  }
  .founder-name {
    font-weight: 400;
    font-size: 27px;
    letter-spacing: 0.5px;
    line-height: 1.1;
  }
  .founder-title {
    font-weight: 300;
    font-size: 12px;
    letter-spacing: 0.3px;
    margin-top: 2px;
  }
  .divider {
    width: 160px; height: 3px;
    background: var(--teal);
    margin: 24px auto 0;
  }
  .contact {
    list-style: none;
    margin-top: 24px;
    color: var(--teal-soft);
    font-size: 9px;
    line-height: 17px;
  }
</style>
</head>
<body>
<main class="sheet">

  <section class="card card--front" aria-label="Business card front">
    <div class="block" style="left:17px;top:17px;width:15px;height:15px;"></div>
    <div class="front-brand">
      <span class="brand-dot"></span>
      <span class="brand-name">HCB</span>
    </div>
    <div class="block" style="left:483px;top:276px;width:17px;height:17px;"></div>
  </section>

  <section class="card card--back" aria-label="Business card back">
    <div class="drawing-area" role="img" aria-label="Faint line drawing of a commercial building"></div>

    <div class="block" style="left:17px;top:17px;width:15px;height:15px;"></div>
    <div class="block" style="left:51px;top:17px;width:96px;height:15px;"></div>
    <div class="block" style="left:17px;top:52px;width:15px;height:95px;"></div>
    <div class="block" style="left:483px;top:163px;width:17px;height:95px;"></div>
    <div class="block" style="left:369px;top:276px;width:96px;height:17px;"></div>
    <div class="block" style="left:483px;top:276px;width:17px;height:17px;"></div>

    <div class="back-brand">
      <span class="brand-dot"></span>
      <span class="brand-name">HCB</span>
    </div>

    <div class="identity">
      <h1 class="founder-name">FOUNDER NAME</h1>
      <p class="founder-title">CO-FOUNDER BUSINESS NAME</p>
      <div class="divider"></div>
      <ul class="contact">
        <li>+00 1234 56789 9101</li>
        <li>123 Dummy Road, Lorem Ipsum, Country</li>
        <li>contact@websitename.com</li>
        <li>www.websitename.com</li>
      </ul>
    </div>
  </section>

</main>
</body>
</html>
```